Dorvelan Swimming & Athletics Center

We need Business Card for a Athletics center
The logo frome the Uploaded Files ( b card fimal)
Οn one side of card we need the logo of company the Contact and the website:
1. Address:(Limassol, Cyprus 12-14 Stavrinelou str,Ano Trimeni,P.C. 4832)

2.Phone number: (+357) 25-704263

3. Mail: info@dorvelanfit.example

3. Website: www.dorvelanfit.example

Οn the other side of the card we need to write the sport of the company:

1. Artistic Gymnastics
2. Swimming
3. Gym - Fitness
4. Programs
5. Dancing
5.Tennis

From the Uploaded Files you can get the logo.In a logo is behind the black color which can be removed from logo.

Υou can use that color you want.
.
Updates

Industry/Entity Type

Business

Font styles to use
Decorative

Colors
0555a3
ffcf3e
3176b5
0692cd
add136
f04a50
000000
cfcfcf
9d9d9d

Requirements
Should not have
• photos with faces
• photo fro the Website:www.dorvelanfit.example

```html
<!DOCTYPE html>
<html lang="en">
<head>
<meta charset="utf-8">
<title>Dorvelan Swimming &amp; Athletics Center – Business Card</title>
<link rel="stylesheet" href="https://fonts.googleapis.com/css2?family=Cinzel:wght@400;700&family=Lato:wght@400;700;900&display=swap">
<style>
  :root {
    --backdrop: #3a3a3a;
    --card: #171717;
    --gold: #ffb12e;
    --gold-light: #ffcf3e;
    --gold-deep: #f39a1e;
    --navy: #2f3470;
    --white: #f2f2f2;
  }
  * { margin: 0; padding: 0; box-sizing: border-box; }
  html, body { width: 1105px; height: 1200px; overflow: hidden; }
  body { background: var(--backdrop); position: relative; font-family: "Lato", sans-serif; color: var(--white); }

  .card {
    position: absolute; left: 196px; width: 720px; height: 412px;
    background: var(--card); border-radius: 20px; overflow: hidden;
  }
  .card--front { top: 145px; }
  .card--back { top: 602px; }

  .corner-art { position: absolute; inset: 0; width: 100%; height: 100%; }

  .brand { position: absolute; display: flex; align-items: center; gap: 18px; }
  .brand__name { font-family: "Lato", sans-serif; font-weight: 900; color: var(--gold); letter-spacing: 2px; line-height: 1; }
  .card--front .brand { right: 42px; top: 76px; }
  .card--front .brand__name { font-size: 55px; }
  .brand__mark { width: 66px; height: 66px; border-radius: 50%; background: var(--gold-light); border: 3px solid var(--white); }

  .holder { position: absolute; left: 44px; top: 180px; }
  .holder__name { font-family: "Cinzel", serif; font-size: 29px; color: var(--gold); line-height: 1; }
  .holder__role { font-family: "Cinzel", serif; font-size: 20px; margin-top: 8px; line-height: 1; }

  .contact { position: absolute; left: 44px; top: 260px; font-size: 18px; line-height: 28px; }
  .contact__row { display: flex; align-items: center; gap: 8px; white-space: nowrap; }
  .contact__icon { width: 17px; height: 17px; flex: none; }
  .contact__gap { width: 10px; }
  .contact__company { color: var(--gold); font-weight: 700; margin-top: 2px; }

  .card--back .brand { left: 0; right: 0; top: 162px; justify-content: center; }
  .card--back .brand__name { font-size: 66px; }

  .sports { position: absolute; left: 0; right: 0; top: 262px; text-align: center; font-size: 20px; line-height: 29px; }
  .sports__dot { color: var(--gold); padding: 0 5px; }
</style>
</head>
<body>

<section class="card card--front" aria-label="Business card front">
  <svg class="corner-art" viewBox="0 0 720 412" aria-hidden="true">
    <defs>
      <linearGradient id="goldFill" x1="0" y1="0" x2="1" y2="1">
        <stop offset="0" stop-color="#ffcf3e"/>
        <stop offset="1" stop-color="#f39a1e"/>
      </linearGradient>
    </defs>
    <path d="M0 0 H166 Q30 33 0 177 Z" fill="var(--navy)"/>
    <path d="M0 0 H148 Q19 25 0 160 Z" fill="url(#goldFill)"/>
    <path d="M720 412 H555 Q690 385 720 238 Z" fill="var(--navy)"/>
    <path d="M720 412 H578 Q702 392 720 262 Z" fill="url(#goldFill)"/>
  </svg>

  <div class="brand">
    <span class="brand__name">DORVELAN</span>
    <span class="brand__mark"></span>
  </div>

  <div class="holder">
    <p class="holder__name">Alex Marlow</p>
    <p class="holder__role">CEO/Founder</p>
  </div>

  <div class="contact">
    <p class="contact__row">
      <svg class="contact__icon" viewBox="0 0 24 24" aria-hidden="true"><path fill="var(--gold)" d="M6.6 10.8a15 15 0 0 0 6.6 6.6l2.2-2.2c.3-.3.7-.4 1-.2 1.1.4 2.3.6 3.6.6.6 0 1 .4 1 1V20c0 .6-.4 1-1 1C10.6 21 3 13.4 3 4c0-.6.4-1 1-1h3.5c.6 0 1 .4 1 1 0 1.2.2 2.4.6 3.6.1.3 0 .7-.2 1z"/></svg>
      (+357) 25-704263
    </p>
    <p class="contact__row">
      <svg class="contact__icon" viewBox="0 0 24 24" aria-hidden="true"><rect x="2" y="5" width="20" height="14" rx="1" fill="var(--gold)"/><path d="M2 6l10 7 10-7" fill="none" stroke="var(--card)" stroke-width="1.8"/></svg>
      info@dorvelanfit.example
      <span class="contact__gap"></span>
      <svg class="contact__icon" viewBox="0 0 24 24" aria-hidden="true"><circle cx="12" cy="12" r="10" fill="var(--gold)"/><path d="M2 12h20M12 2c3 3 3 17 0 20M12 2c-3 3-3 17 0 20" fill="none" stroke="var(--card)" stroke-width="1.5"/></svg>
      www.dorvelanfit.example
    </p>
    <p class="contact__company">DORVELAN ATHLETICS CENTER</p>
    <p class="contact__row">Limassol, Cyprus 12-14 Stavrinelou str,Ano Trimeni,P.C. 4832</p>
  </div>
</section>

<section class="card card--back" aria-label="Business card back">
  <div class="brand">
    <span class="brand__name">DORVELAN</span>
  </div>
  <div class="sports">
    <p>Artistic Gymnastics<span class="sports__dot">•</span>Swimming</p>
    <p>Gym - Fitness<span class="sports__dot">•</span>Programs<span class="sports__dot">•</span>Dancing<span class="sports__dot">•</span>Tennis</p>
  </div>
</section>

</body>
</html>
```